BrimFalcon Business Cards

We have a defined brand. Please visit our website to get a feel for the product and the color pallets. www.brimfalcon-demo.com

We need an updated, world class business card design. (See the attached existing card design). Please utilize BOTH sides of the card as shown and be creative with the layout. I do want the horse head icon to be positioned as it is with the existing card.

The remainder of the layout can be customized and I also want it vertically oriented.

Attached are the logo files and please use the colors as follows:
Green - #A5CE39
Tan - #CDBD99
Black

Feel free to play with the colors.

```html
<!DOCTYPE html>
<html lang="en">
<head>
<meta charset="utf-8">
<title>BrimFalcon Business Card</title>
<link href="https://fonts.googleapis.com/css2?family=Mulish:wght@400;600;700;800&display=swap" rel="stylesheet">
<style>
  :root {
    --green: #a5ce39;
    --ink: #222222;
    --text: #333333;
    --paper: #ffffff;
    --backdrop: #e9e7e2;
    --faint: #f2f2f0;
  }
  * { margin: 0; padding: 0; box-sizing: border-box; }
  html, body { width: 1200px; height: 848px; overflow: hidden; }
  body {
    background: var(--backdrop);
    font-family: "Mulish", sans-serif;
    position: relative;
  }
  .card {
    position: absolute;
    top: 127px;
    width: 335px;
    height: 586px;
    overflow: hidden;
    box-shadow: 0 4px 14px rgba(0,0,0,0.18);
  }
  .card-front { left: 242px; background: var(--paper); }
  .card-back { left: 612px; background: var(--ink); }

  /* front */
  .brand { position: absolute; top: 38px; left: 0; width: 100%; text-align: center; }
  .brand-row { display: flex; align-items: center; justify-content: center; gap: 8px; }
  .brand-dot { width: 34px; height: 34px; border-radius: 50%; background: var(--ink); }
  .brand-name { font-size: 30px; font-weight: 800; color: var(--ink); letter-spacing: 0.5px; }
  .brand-tagline {
    margin-top: 4px; margin-left: 42px;
    font-size: 11.5px; font-weight: 700; letter-spacing: 3.4px; color: var(--ink);
  }
  .faint-mark {
    position: absolute; left: 10px; top: 270px;
    width: 300px; height: 300px; border-radius: 50%;
    background: var(--faint);
  }
  .name-band {
    position: absolute; top: 313px; left: 0; width: 100%; height: 49px;
    background: var(--green);
  }
  .name-panel {
    position: absolute; left: 33px; right: 33px; top: 0; bottom: 0;
    background: var(--ink); text-align: center;
  }
  .person-name { font-size: 22px; font-weight: 800; color: var(--green); line-height: 1; margin-top: 5px; }
  .person-title { font-size: 12.5px; color: #fff; margin-top: 4px; }
  .contact { position: absolute; left: 0; width: 100%; text-align: center; color: var(--text); font-size: 14px; }
  .location { top: 390px; }
  .location p { line-height: 21px; }
  .accent { color: var(--green); }
  .icon { display: inline-block; vertical-align: middle; }
  .icon-row { display: flex; justify-content: center; gap: 3px; margin-bottom: 4px; }
  .lines { top: 465px; }
  .lines p { line-height: 21px; }

  /* back */
  .back-rule {
    position: absolute; left: 37px; top: 121px; width: 1px; height: 344px;
    background: var(--green);
  }
  .back-tagline {
    position: absolute; left: 28px; top: 207px; height: 173px; width: 18px;
    writing-mode: vertical-rl; background: var(--ink);
    font-size: 12px; font-weight: 700; letter-spacing: 1.2px; color: var(--green);
    text-align: center; line-height: 18px;
  }
  .back-name {
    position: absolute; left: 74px; top: 122px;
    writing-mode: vertical-rl;
    font-size: 50px; font-weight: 700; color: #fff; letter-spacing: 1px; line-height: 60px;
  }
  .back-mark {
    position: absolute; left: 143px; top: 232px; width: 115px; height: 115px;
    border-radius: 50%; background: #4a4a4a;
  }
</style>
</head>
<body>
  <section class="card card-front">
    <div class="faint-mark"></div>
    <header class="brand">
      <div class="brand-row">
        <span class="brand-dot"></span>
        <span class="brand-name">BrimFalcon</span>
      </div>
      <div class="brand-tagline">Performance Driven EVs</div>
    </header>

    <div class="name-band">
      <div class="name-panel">
        <div class="person-name">DANA VERHOEVEN</div>
        <div class="person-title">President &amp; CEO</div>
      </div>
    </div>

    <div class="contact location">
      <svg class="icon" width="18" height="18" viewBox="0 0 18 18">
        <circle cx="9" cy="9" r="8" fill="none" stroke="var(--green)" stroke-width="1"/>
        <path d="M9 4.2a3 3 0 0 0-3 3c0 2.2 3 5.8 3 5.8s3-3.6 3-5.8a3 3 0 0 0-3-3z" fill="var(--green)"/>
        <circle cx="9" cy="7.2" r="1.1" fill="#fff"/>
      </svg>
      <p>Northfield, Saskatchewan</p>
      <p class="accent">Canada</p>
    </div>

    <div class="contact lines">
      <div class="icon-row">
        <svg class="icon" width="18" height="18" viewBox="0 0 18 18">
          <circle cx="9" cy="9" r="8" fill="none" stroke="var(--green)"/>
          <path d="M6 5l1.6-.4 1 2.2-1 .8a5 5 0 0 0 2.6 2.6l.8-1 2.2 1L12.8 12C9 12.5 5.5 9 6 5z" fill="var(--green)"/>
        </svg>
        <svg class="icon" width="18" height="18" viewBox="0 0 18 18">
          <circle cx="9" cy="9" r="8" fill="none" stroke="var(--green)"/>
          <rect x="5" y="6" width="8" height="6" fill="var(--green)"/>
          <path d="M5 6l4 3.2L13 6" fill="none" stroke="#fff" stroke-width="0.9"/>
        </svg>
        <svg class="icon" width="18" height="18" viewBox="0 0 18 18">
          <circle cx="9" cy="9" r="8" fill="none" stroke="var(--green)"/>
          <circle cx="9" cy="9" r="4.6" fill="var(--green)"/>
          <path d="M4.4 9h9.2M9 4.4c-2 2.6-2 6.6 0 9.2M9 4.4c2 2.6 2 6.6 0 9.2" fill="none" stroke="#fff" stroke-width="0.7"/>
        </svg>
      </div>
      <p>306.555.0142</p>
      <p>dana@brimfalcon-demo.com</p>
      <p><span class="accent">brimfalconlabs-demo</span>.com</p>
    </div>
  </section>

  <section class="card card-back">
    <div class="back-rule"></div>
    <div class="back-tagline">MOBILITY REIMAGINED</div>
    <div class="back-name">BrimFalcon</div>
    <div class="back-mark"></div>
  </section>
</body>
</html>
```